Velmora Diagnostics Website

Project Description – Velmora Website Design
We need a clean, modern, and professional website for Velmora Diagnostics, a Ashgrove Hollis University of Dunmere spin-out focused on early cancer detection. Our first product, GlandSURE™, is a urine-based risk assessment test for pancreatic cancer, supported by strong clinical validation and partnerships with leading hospitals.

The site should:

Communicate trust, innovation, and clinical credibility.
Feature a clear value proposition on the home page with strong calls to action for investors, clinicians, and partners.
Showcase our technology, science, and clinical evidence in a way that is accessible but authoritative.
Highlight our university heritage, team, and collaborators.
Include sections for products/services, news/press, and contact forms.
Be fully responsive, WordPress compatible, SEO-friendly, and WCAG 2.1 AA accessible.

We want a minimalist, elegant design with subtle animations, strong visuals (e.g., science/biotech imagery), and a clear structure for future growth.
Deliverables should include editable design files (Figma/Sketch/Adobe XD) and a style guide.

```html
<!DOCTYPE html>
<html lang="en">
<head>
<meta charset="utf-8">
<title>Velmora Diagnostics</title>
<link rel="stylesheet" href="https://fonts.googleapis.com/css2?family=Poppins:wght@400;500;600;700&display=swap">
<style>
:root{
  --blue:#3a86d6;
  --blue-dark:#2f73c0;
  --sky:#5bb8ec;
  --yellow:#f6c431;
  --orange:#f58a2a;
  --cream:#fffbea;
  --ink:#161616;
  --grey:#5a5a5a;
  --line:#d9d9d9;
  --white:#ffffff;
}
*{box-sizing:border-box;margin:0;padding:0}
html,body{width:1200px;height:2995px;overflow:hidden;background:var(--white)}
body{font-family:"Poppins",sans-serif;color:var(--ink)}
.page{position:relative;z-index:0;width:1200px;height:2995px;overflow:hidden;background:var(--white)}
.abs{position:absolute}

/* header */
.brand{display:flex;align-items:center;gap:12px;font-weight:500;letter-spacing:1.5px}
.brand-dot{width:26px;height:26px;border-radius:50%}
.header-brand{left:60px;top:28px;font-size:22px;color:var(--blue)}
.header-brand .brand-dot{background:var(--yellow)}
.call{left:978px;top:22px;display:flex;align-items:center;gap:8px}
.call-icon{width:36px;height:36px;border-radius:50%;border:2px solid var(--yellow);display:flex;align-items:center;justify-content:center}
.call small{display:block;font-size:11px;line-height:14px}
.call strong{display:block;font-size:17px;font-weight:500;line-height:20px}
.top-arc{z-index:-1;left:590px;top:-250px;width:520px;height:520px;border-radius:50%;border:40px solid #eef3fb}
.nav{left:0;top:84px;width:1200px;height:43px;border-bottom:1px solid var(--line)}
.nav a{position:absolute;top:0;height:42px;line-height:42px;font-size:13px;color:var(--blue);text-decoration:none}
.nav .active{left:60px;width:97px;text-align:center;background:var(--yellow);color:var(--blue)}
.quote{left:952px;top:84px;width:188px;height:41px;background:var(--yellow);font-size:14px;font-weight:500;text-align:center;line-height:41px;color:var(--ink)}

/* hero */
.hero-glow{z-index:-1;left:-170px;top:128px;width:445px;height:300px;border-radius:0 0 50% 50%;background:var(--cream)}
.hero-title{left:60px;top:236px;font-size:46px;line-height:52px;font-weight:700;color:var(--blue)}
.hero-sub{left:61px;top:403px;width:420px;font-size:16px;line-height:24px;color:#333}
.btn-pill{display:flex;align-items:center;justify-content:center;border-radius:30px;font-weight:500}
.hero-cta{left:60px;top:473px;width:157px;height:40px;background:var(--yellow);font-size:14px;gap:18px}
.follow{left:61px;top:624px;display:flex;align-items:center;gap:10px;font-size:11px}
.follow-rule{width:56px;height:1px;background:var(--ink)}
.follow-circle{width:31px;height:31px;border-radius:50%;border:1.5px solid var(--blue)}

/* differentiators */
.diff-box{left:150px;top:781px;width:900px;height:217px;border:2px solid var(--blue);border-radius:24px}
.diff-title{left:460px;top:762px;width:280px;height:40px;background:var(--white);text-align:center;font-size:25px;font-weight:600;color:var(--blue);line-height:40px}
.diff-dot{width:12px;height:12px;border-radius:50%;background:var(--yellow);top:775px}
.diff-item{top:834px;width:200px;text-align:center;font-size:17px;font-weight:500;line-height:23px}
.diff-icon{width:70px;height:70px;border-radius:50%;background:var(--sky);margin:0 auto 19px;display:flex;align-items:center;justify-content:center}

/* about */
.about-band{left:0;top:1073px;width:1200px;height:503px;background:var(--cream)}
.about-title{left:616px;top:1137px;font-size:40px;font-weight:600;color:var(--blue)}
.about-text{left:616px;top:1197px;width:430px;font-size:12.5px;line-height:20px;color:var(--grey)}
.feature{left:614px;display:flex;gap:16px}
.feature-icon{width:62px;height:62px;border:1px solid #c9d7ea;border-radius:8px;background:var(--white);display:flex;align-items:center;justify-content:center;flex:none}
.feature h3{font-size:19px;font-weight:500;margin-top:-3px}
.feature p{font-size:13px;line-height:20px;color:var(--grey);margin-top:8px;width:300px}

/* product */
.prod-title{left:236px;top:1830px;font-size:24px;font-weight:600}
.prod-sub{left:238px;top:1872px;width:300px;font-size:14px;line-height:21px;font-weight:500;color:#444}
.prod-text{left:238px;top:1921px;width:360px;font-size:13px;line-height:20px;color:var(--grey)}
.prod-btn{left:237px;top:2020px;width:127px;height:40px;background:var(--yellow);font-size:15px}

/* news */
.news-title{left:0;top:2200px;width:1200px;text-align:center;font-size:38px;font-weight:600;color:var(--blue)}
.card{top:2280px;width:349px;text-align:center}
.card-photo{height:203px;border-radius:50px}
.card h3{font-size:19px;font-weight:500;margin-top:22px}
.card p{font-size:13px;line-height:22px;color:var(--grey);margin:12px auto 0;width:270px}
.card .btn-pill{width:135px;height:37px;margin:20px auto 0;background:var(--orange);color:var(--white);font-size:15px}

/* footer */
.footer{left:0;top:2711px;width:1200px;height:284px;background:var(--blue);color:var(--white)}
.footer-brand{left:60px;top:2754px;font-size:22px;color:var(--white)}
.footer-brand .brand-dot{background:var(--white)}
.foot-head{top:2752px;font-size:19px;font-weight:600;color:var(--yellow)}
.foot-links{left:426px;top:2792px;list-style:none;font-size:13px;line-height:24px;color:var(--white)}
.foot-contact{left:790px;font-size:13px;display:flex;align-items:center;gap:12px;color:var(--white)}
.foot-rule{left:60px;top:2942px;width:1080px;height:1px;background:rgba(255,255,255,.3)}
.copyright{left:0;top:2960px;width:1200px;text-align:center;font-size:12px;color:var(--white)}
</style>
</head>
<body>
<div class="page">

  <!-- header -->
  <div class="abs top-arc"></div>
  <div class="abs hero-glow"></div>
  <div class="abs brand header-brand"><span class="brand-dot"></span>Velmora DX</div>
  <div class="abs call">
    <span class="call-icon">
      <svg width="20" height="20" viewBox="0 0 24 24"><path d="M6.6 10.8a15 15 0 0 0 6.6 6.6l2.2-2.2c.3-.3.7-.4 1-.2 1.1.4 2.3.6 3.6.6.6 0 1 .4 1 1V20c0 .6-.4 1-1 1A17 17 0 0 1 3 4c0-.6.4-1 1-1h3.5c.6 0 1 .4 1 1 0 1.3.2 2.5.6 3.6.1.3 0 .7-.2 1z" fill="var(--yellow)"/></svg>
    </span>
    <div><small>Call Us On</small><strong>123-456-7890</strong></div>
  </div>
  <nav class="abs nav">
    <a class="active" href="#">Home</a>
    <a href="#" style="left:188px">About Us</a>
    <a href="#" style="left:293px">Services</a>
    <a href="#" style="left:394px">Contact Us</a>
  </nav>
  <div class="abs quote">GET AN INSTANT QUOTE</div>

  <!-- hero -->
  <svg class="abs" style="left:0;top:128px" width="1200" height="600" viewBox="0 0 1200 600">
    <defs>
      <linearGradient id="heroPhoto" x1="0" y1="0" x2="1" y2="1">
        <stop offset="0" stop-color="#dfe6ee"/>
        <stop offset=".5" stop-color="#c4ccd6"/>
        <stop offset="1" stop-color="#eef1f4"/>
      </linearGradient>
    </defs>
    <circle cx="878" cy="203" r="357" fill="none" stroke="var(--yellow)" stroke-width="16"/>
    <path d="M649 476 A357 357 0 0 1 878 -154" fill="none" stroke="var(--blue)" stroke-width="16"/>
    <circle cx="878" cy="203" r="343" fill="url(#heroPhoto)" role="img" aria-label="Photo of a scientist looking into a laboratory microscope"/>
    <circle cx="576" cy="331" r="17" fill="var(--yellow)" opacity=".55"/>
    <circle cx="963" cy="540" r="37" fill="#c9dcf2" opacity=".8"/>
  </svg>
  <h1 class="abs hero-title">Lighting the Way<br>to Early Cancer<br>Detection</h1>
  <p class="abs hero-sub">Non-invasive, urine-based diagnostics for pancreatic cancer, backed by clinical validation.</p>
  <div class="abs btn-pill hero-cta">CONTACT US
    <svg width="26" height="26" viewBox="0 0 26 26"><circle cx="13" cy="13" r="11" fill="none" stroke="var(--ink)" stroke-width="2.2"/><path d="M7 13h11M13.5 8.5 18 13l-4.5 4.5" fill="none" stroke="var(--ink)" stroke-width="2.2" stroke-linecap="round" stroke-linejoin="round"/></svg>
  </div>
  <div class="abs follow">Follow Us <span class="follow-rule"></span><span class="follow-circle"></span></div>

  <!-- differentiators -->
  <div class="abs diff-box"></div>
  <h2 class="abs diff-title">Key differentiators</h2>
  <div class="abs diff-dot" style="left:425px"></div>
  <div class="abs diff-dot" style="left:758px"></div>
  <div class="abs diff-item" style="left:170px">
    <div class="diff-icon"><svg width="40" height="40" viewBox="0 0 40 40" fill="none" stroke="#fff" stroke-width="2"><circle cx="20" cy="20" r="14"/><path d="M10 30 30 10M14 20l4 4 8-9"/></svg></div>
    Non-invasive,<br>painless
  </div>
  <div class="abs diff-item" style="left:381px">
    <div class="diff-icon"><svg width="40" height="40" viewBox="0 0 40 40" fill="none" stroke="#fff" stroke-width="2"><rect x="8" y="14" width="22" height="16" rx="2"/><path d="M12 14v-4h14v4M12 20h8M12 25h6"/><rect x="26" y="18" width="6" height="14" rx="3"/></svg></div>
    Precision<br>biomarkers
  </div>
  <div class="abs diff-item" style="left:594px">
    <div class="diff-icon"><svg width="40" height="40" viewBox="0 0 40 40" fill="none" stroke="#fff" stroke-width="2"><circle cx="20" cy="17" r="9"/><path d="M16 26v6h8v-6M20 10v14M15 14l5 3 5-3M20 4v2M9 8l2 2M31 8l-2 2"/></svg></div>
    AI-powered<br>insights
  </div>
  <div class="abs diff-item" style="left:808px">
    <div class="diff-icon"><svg width="40" height="40" viewBox="0 0 40 40" fill="none" stroke="#fff" stroke-width="2"><path d="M6 15 20 7l14 8zM9 15v15M15 15v15M25 15v15M31 15v15M6 32h28"/><circle cx="20" cy="21" r="3"/></svg></div>
    university spin-out<br>heritage
  </div>

  <!-- about -->
  <div class="abs about-band"></div>
  <svg class="abs" style="left:0;top:1100px" width="560" height="700" viewBox="0 1100 560 700">
    <defs>
      <linearGradient id="aboutPhoto" x1="0" y1="0" x2="1" y2="1">
        <stop offset="0" stop-color="#d5dbe2"/>
        <stop offset=".6" stop-color="#eceef1"/>
        <stop offset="1" stop-color="#b9c2cc"/>
      </linearGradient>
    </defs>
    <circle cx="209" cy="1448" r="322" fill="none" stroke="var(--yellow)" stroke-width="14"/>
    <path d="M-100 1335 A329 329 0 0 1 530 1505" fill="none" stroke="var(--blue)" stroke-width="14"/>
    <circle cx="209" cy="1448" r="314" fill="url(#aboutPhoto)" role="img" aria-label="Photo of a smiling scientist in a lab coat holding a tablet in the laboratory"/>
  </svg>
  <h2 class="abs about-title">About Us</h2>
  <p class="abs about-text">Velmora Diagnostics was born as a spin-out from Ashgrove Hollis University of Dunmere, rooted in pioneering research from the Carrow Oncology Institute. Our origins lie in a mission-driven collaboration between academic scientists and clinicians, united by the goal of transforming how cancer is detected and monitored.</p>
  <div class="abs feature" style="top:1330px">
    <div class="feature-icon"><svg width="32" height="32" viewBox="0 0 32 32" fill="none" stroke="var(--blue)" stroke-width="1.6"><circle cx="15" cy="17" r="11"/><circle cx="15" cy="17" r="6"/><circle cx="15" cy="17" r="1.5"/><path d="M15 17 27 5M23 5h4v4"/></svg></div>
    <div><h3>Our Mission</h3><p>Lorem Ipsum has been the industry's standard dummy text ever since the 1500s...</p></div>
  </div>
  <div class="abs feature" style="top:1428px">
    <div class="feature-icon"><svg width="32" height="32" viewBox="0 0 32 32" fill="none" stroke="var(--blue)" stroke-width="1.6"><path d="M3 16s5-8 13-8 13 8 13 8-5 8-13 8S3 16 3 16z"/><circle cx="16" cy="16" r="4"/><path d="M16 3v2M16 27v2M6 6l1.5 1.5M26 6l-1.5 1.5"/></svg></div>
    <div><h3>Our vission</h3><p>Lorem Ipsum has been the industry's standard dummy text ever since the 1500s.</p></div>
  </div>

  <!-- product -->
  <h2 class="abs prod-title">GlandSURE™</h2>
  <p class="abs prod-sub">pancreatic cancer risk assessment &amp; surveillance.</p>
  <p class="abs prod-text">Lorem Ipsum has been the industry's standard dummy text ever since the 1500s, when an unknown printer took a galley of type and scrambled it to make a type specimen book.</p>
  <div class="abs btn-pill prod-btn">Read More</div>
  <svg class="abs" style="left:665px;top:1764px" width="376" height="376" viewBox="0 0 376 376">
    <defs>
      <radialGradient id="organ" cx=".5" cy=".5" r=".6">
        <stop offset="0" stop-color="#1f6ee0"/>
        <stop offset=".7" stop-color="#0a3a9a"/>
        <stop offset="1" stop-color="#041a52"/>
      </radialGradient>
    </defs>
    <circle cx="188" cy="188" r="188" fill="url(#organ)" role="img" aria-label="Illustration of the human abdomen with the pancreas highlighted in red"/>
  </svg>

  <!-- news -->
  <h2 class="abs news-title">News &amp; Events</h2>
  <article class="abs card" style="left:60px">
    <div class="card-photo" role="img" aria-label="Photo of researchers working at laboratory computers" style="background:linear-gradient(135deg,#c9d2db,#e7ebef 55%,#9aa7b4)"></div>
    <h3>Lorem ipsum</h3>
    <p>Lorem Ipsum is simply dummy text of the printing and typesetting industry.</p>
    <div class="btn-pill">READ MORE</div>
  </article>
  <article class="abs card" style="left:426px">
    <div class="card-photo" role="img" aria-label="Photo of a scientist taking notes beside a microscope" style="background:linear-gradient(135deg,#d8dde2,#f0f1f3 50%,#a9b1ba)"></div>
    <h3>lorem ipsum</h3>
    <p>Lorem Ipsum is simply dummy text of the printing and typesetting industry.</p>
    <div class="btn-pill">READ MORE</div>
  </article>
  <article class="abs card" style="left:791px">
    <div class="card-photo" role="img" aria-label="Photo of lab technicians in masks handling test tubes" style="background:linear-gradient(135deg,#cfd8e0,#e9eef2 50%,#8fa8c4)"></div>
    <h3>loram ipsum</h3>
    <p>Lorem Ipsum is simply dummy text of the printing and typesetting industry.</p>
    <div class="btn-pill">READ MORE</div>
  </article>

  <!-- footer -->
  <footer class="abs footer"></footer>
  <div class="abs brand footer-brand"><span class="brand-dot"></span>Velmora DX</div>
  <h4 class="abs foot-head" style="left:426px">Quick link</h4>
  <ul class="abs foot-links">
    <li>Home</li><li>About Us</li><li>Services</li><li>Contact Us</li>
  </ul>
  <h4 class="abs foot-head" style="left:792px">Contact Us</h4>
  <div class="abs foot-contact" style="top:2798px">
    <svg width="20" height="20" viewBox="0 0 24 24"><path d="M6.6 10.8a15 15 0 0 0 6.6 6.6l2.2-2.2c.3-.3.7-.4 1-.2 1.1.4 2.3.6 3.6.6.6 0 1 .4 1 1V20c0 .6-.4 1-1 1A17 17 0 0 1 3 4c0-.6.4-1 1-1h3.5c.6 0 1 .4 1 1 0 1.3.2 2.5.6 3.6.1.3 0 .7-.2 1z" fill="var(--yellow)"/></svg>
    <span style="font-size:14px">123 456 7890</span>
  </div>
  <div class="abs foot-contact" style="top:2838px">
    <svg width="20" height="16" viewBox="0 0 20 16"><rect width="20" height="16" rx="2" fill="var(--yellow)"/><path d="M1 2l9 7 9-7" fill="none" stroke="var(--blue)" stroke-width="1.6"/></svg>
    <span>info@velmoradx.com</span>
  </div>
  <div class="abs foot-contact" style="top:2874px;align-items:flex-start">
    <svg width="20" height="24" viewBox="0 0 20 24"><path d="M10 1a7 7 0 0 0-7 7c0 5 7 12 7 12s7-7 7-12a7 7 0 0 0-7-7z" fill="none" stroke="var(--yellow)" stroke-width="2"/><circle cx="10" cy="8" r="2.5" fill="var(--yellow)"/><ellipse cx="10" cy="22" rx="6" ry="1.5" fill="var(--yellow)"/></svg>
    <div>Velmora DX<br><span style="font-size:11px">101 Lorem ipsum simple text</span></div>
  </div>
  <div class="abs foot-rule"></div>
  <p class="abs copyright">©Velmora DX. -2022 All rights reserved.</p>

</div>
</body>
</html>
```